CoinHarbor Rangers (Ledger Meadow)
A website dedicated to crypto education. We are a new company focused on blockchain edutainment (education and interesting and entertaining content about the blockchain space). We want a fun, clean/minimalist and modern website that is made up of an education platform which could be a website in it’s own right. It will be the reference point for our users/community for all of our other blockchain based content in the CHR website ecosystem which will be covering; crypto news, digital asset investing (including a technical and fundamental analysis subscription service), blockchain business solutions and an NFT section that will cover creative art projects (art, music, gaming and more). To feature a logins and payment system which may need a shopping basket set up for tutorial/educational platform that is accessed via the website, NFT page with sub-categories: education and NFT and metaverse/virtual world and merchandise shopping page which is Web 3.0 enabled (able to link to a VaultPorch, Keel Purse etc , digital asset education page featuring blog and newsletter subscriptions links, A social media page where people can access videos, podcasts and our presence on other platforms such as Chirpline, Snapmosaic, Hubbleroom, Wirepost etc.
Number of Pages Required
5+ page

```html
<!DOCTYPE html>
<html lang="en">
<head>
<meta charset="utf-8">
<title>CoinHarbor Rangers</title>
<link href="https://fonts.googleapis.com/css2?family=Outfit:wght@400;500;600&family=DM+Sans:wght@400;500;700&display=swap" rel="stylesheet">
<style>
:root{
  --navy:#0b0936;
  --navy-deep:#07062a;
  --purple:#8d12b9;
  --violet:#5b1fd6;
  --blue:#1717d9;
  --pink:#e2459b;
  --white:#ffffff;
  --ink:#0b0b14;
  --muted:#d9d6ee;
  --btn-dark:#2b2740;
}
*{box-sizing:border-box;margin:0;padding:0}
html,body{width:1200px;height:3608px;overflow:hidden}
body{
  position:relative;
  font-family:"DM Sans",sans-serif;
  color:var(--white);
  background:
    radial-gradient(ellipse 420px 380px at 0 560px,rgba(170,20,190,.55),transparent 70%),
    radial-gradient(ellipse 600px 400px at 720px 80px,rgba(40,40,220,.45),transparent 70%),
    radial-gradient(ellipse 700px 360px at 600px 2990px,rgba(150,30,200,.5),transparent 70%),
    radial-gradient(ellipse 500px 400px at 1200px 2600px,rgba(40,30,200,.35),transparent 70%),
    linear-gradient(180deg,#14104a 0,var(--navy) 700px,var(--navy-deep) 1300px,var(--navy) 2100px,#0d0c52 2700px,#150b5c 3050px,var(--navy-deep) 3250px);
}
.abs{position:absolute}
h1,h2,h3{font-family:"Outfit",sans-serif;font-weight:500}
.pill{position:absolute;display:flex;align-items:center;justify-content:center;border-radius:30px;font-weight:700;font-size:15px;white-space:nowrap}
.pill-outline{border:2px solid var(--white);color:var(--white)}
.pill-white{background:var(--white);color:var(--ink)}

/* header */
.brand{position:absolute;display:flex;align-items:center;gap:8px;font-family:"Outfit",sans-serif;font-weight:600;font-size:23px;white-space:nowrap}
.brand-dot{width:48px;height:48px;border-radius:50%;background:var(--white)}
.nav a{position:absolute;top:33px;font-size:14px;color:var(--white);text-decoration:none}
.nav a.active{color:var(--pink)}
.cart{position:absolute;left:1050px;top:26px;width:36px;height:36px;border-radius:50%;background:var(--white);border:3px solid #c21a8e}
.cart-count{position:absolute;left:1074px;top:24px;width:14px;height:14px;border-radius:50%;background:var(--white);color:var(--ink);font-size:9px;display:flex;align-items:center;justify-content:center;border:1px solid var(--ink)}

/* hero */
.hero-title{position:absolute;left:112px;top:180px;font-size:46px;line-height:60px;white-space:nowrap}
.hero-text{position:absolute;left:112px;top:318px;width:480px;font-size:15px;line-height:26px;color:var(--muted)}
.btn-sq{position:absolute;top:393px;height:48px;display:flex;align-items:center;justify-content:center;font-weight:700;font-size:16px;clip-path:polygon(0 0,92% 0,100% 22%,100% 100%,0 100%)}
.hero-art{position:absolute;left:628px;top:140px;width:440px;height:330px;border-radius:24px;
  background:linear-gradient(135deg,rgba(150,40,210,.45),rgba(50,40,200,.4));}

/* ecosystem */
.eco{position:absolute;left:112px;top:618px;width:1140px;height:477px;border-radius:32px;border:3px solid;border-color:#7a18b8 transparent #2222e0 #5a20d0;background:rgba(8,6,40,.6)}
.eco h2{position:absolute;left:50px;top:45px;font-size:38px}
.eco-col{position:absolute;top:205px;width:280px}
.eco-icon{width:62px;height:62px;border-radius:50%;background:linear-gradient(135deg,#6e1ad0,#3a1fd8);display:flex;align-items:center;justify-content:center}
.eco-col h3{font-size:23px;margin-top:18px;white-space:nowrap}
.eco-col p{font-size:15px;line-height:22px;margin-top:12px;color:var(--muted)}
.learn{display:flex;align-items:center;gap:6px;margin-top:18px;font-weight:700;font-size:14px}

/* tutorials */
.section-title{position:absolute;left:0;width:1200px;text-align:center;font-size:39px}
.card{position:absolute;width:310px;height:338px;border-radius:8px;overflow:hidden}
.card-social{position:absolute;left:12px;top:14px;display:flex;gap:5px}
.card-social span{height:22px;padding:0 7px;border-radius:11px;background:var(--ink);font-size:9px;display:flex;align-items:center}
.card-badge{position:absolute;right:14px;top:12px;height:30px;width:62px;border-radius:15px;background:var(--white);color:var(--ink);font-size:14px;display:flex;align-items:center;justify-content:center;font-weight:500}
.card-foot{position:absolute;left:16px;right:16px;bottom:22px;height:72px;background:var(--white);border-radius:4px;color:var(--ink)}
.card-foot small{position:absolute;left:15px;top:13px;font-size:10px;font-weight:700}
.card-foot strong{position:absolute;left:15px;top:30px;font-family:"Outfit",sans-serif;font-weight:500;font-size:24px;white-space:nowrap}
.watch{position:absolute;right:12px;top:14px;height:42px;width:122px;border-radius:21px;background:var(--ink);color:var(--white);font-size:14px;display:flex;align-items:center;justify-content:center;gap:8px;white-space:nowrap}

/* education band */
.edu-band{position:absolute;left:0;top:2108px;width:1200px;height:312px;background:linear-gradient(180deg,rgba(30,30,110,.35),rgba(20,20,90,.55),rgba(30,30,110,.35))}
.edu-text{position:absolute;left:200px;top:2228px;width:800px;text-align:center;font-size:15px;line-height:26px;color:var(--muted)}

/* nft carousel */
.nft{position:absolute;background:var(--white);border-radius:4px;overflow:hidden;color:var(--ink)}
.nft-art{width:100%}
.nft-cap{text-align:center;font-family:"Outfit",sans-serif;font-weight:500;white-space:nowrap}
.dot{position:absolute;top:3071px;width:13px;height:13px;border-radius:50%;background:var(--white)}

/* footer */
.foot-head{position:absolute;font-weight:700;font-size:16px}
.foot-list{position:absolute;list-style:none;font-size:15px}
.news-title{position:absolute;left:584px;top:3242px;font-size:30px;white-space:nowrap}
.news-input{position:absolute;left:586px;top:3310px;width:322px;height:38px;border-bottom:1px solid var(--muted);font-size:14px;color:var(--muted);padding-top:6px}
.wallet{position:absolute;top:3432px;display:flex;align-items:center;gap:10px;font-family:"Outfit",sans-serif;font-weight:600;font-size:19px;white-space:nowrap}
.wallet i{display:block;width:44px;height:44px;border-radius:50%}
.pay{position:absolute;top:3553px;left:826px;display:flex;gap:4px}
.pay span{width:35px;height:24px;border-radius:3px;background:var(--white)}
</style>
</head>
<body>

<header>
  <div class="brand" style="left:112px;top:16px"><span class="brand-dot"></span>CoinHarbor Rangers</div>
  <nav class="nav">
    <a class="active" style="left:476px">Home</a>
    <a style="left:564px">About</a>
    <a style="left:648px">Nft</a>
    <a style="left:712px">Invaders</a>
    <a style="left:814px">Contact</a>
  </nav>
  <div class="pill pill-outline" style="left:916px;top:22px;width:94px;height:42px;font-size:14px">Sign Up</div>
  <div class="cart"><svg width="30" height="30" viewBox="0 0 30 30"><path d="M8 10h2l2 8h8l2-6H11" fill="none" stroke="#0b0b14" stroke-width="2"/><circle cx="13" cy="21" r="1.4"/><circle cx="19" cy="21" r="1.4"/></svg></div>
  <div class="cart-count">0</div>
</header>

<section class="hero">
  <h1 class="hero-title">Welcome To<br>CoinHarbor Rangers</h1>
  <p class="hero-text">Lorem ipsum dolor sit amet, consectetur adipiscing elit, sed do eius-mod tempor incididunt ut labore et dolore magna aliqua.</p>
  <div class="btn-sq" style="left:112px;width:138px;background:var(--purple)">Get Started</div>
  <div class="btn-sq" style="left:275px;width:138px;background:var(--btn-dark)">Earn Tokens</div>
  <div class="hero-art" role="img" aria-label="Hero illustration: two pixel-art characters with a neon glow"></div>
</section>

<section class="eco">
  <h2>CHR Ecosystem</h2>
  <div class="pill" style="left:50px;top:116px;width:148px;height:46px;background:var(--purple);font-size:14px">CHR Ecosystem</div>
  <div class="pill pill-outline" style="left:214px;top:116px;width:208px;height:46px;font-size:14px">Community Ecosystem</div>
  <div class="eco-col" style="left:50px">
    <div class="eco-icon"><svg width="30" height="30" viewBox="0 0 30 30" fill="none" stroke="#fff" stroke-width="1.6"><rect x="5" y="5" width="20" height="20" rx="2"/><path d="M9 11h12M9 15h5M9 19h5M17 15h4v4h-4z"/></svg></div>
    <h3>Crypto News</h3>
    <p>Lorem ipsum dolor sit amet, consec-tetur adipiscing elit, sed do eiusmod tempor incididunt</p>
    <div class="learn">Learn More <svg width="13" height="13" viewBox="0 0 13 13"><circle cx="6.5" cy="6.5" r="6.5" fill="#fff"/><path d="M5 3.5l3 3-3 3" stroke="#0b0936" stroke-width="1.6" fill="none"/></svg></div>
  </div>
  <div class="eco-col" style="left:364px">
    <div class="eco-icon"><svg width="30" height="30" viewBox="0 0 30 30" fill="none" stroke="#fff" stroke-width="1.6"><circle cx="15" cy="10" r="6"/><path d="M15 16v8M8 24h14"/></svg></div>
    <h3>Digital asset investing</h3>
    <p>Lorem ipsum dolor sit amet, consec-tetur adipiscing elit, sed do eiusmod tempor incididunt</p>
    <div class="learn">Learn More <svg width="13" height="13" viewBox="0 0 13 13"><circle cx="6.5" cy="6.5" r="6.5" fill="#fff"/><path d="M5 3.5l3 3-3 3" stroke="#0b0936" stroke-width="1.6" fill="none"/></svg></div>
  </div>
  <div class="eco-col" style="left:678px">
    <div class="eco-icon"><svg width="30" height="30" viewBox="0 0 30 30" fill="none" stroke="#fff" stroke-width="1.6"><circle cx="15" cy="15" r="3"/><circle cx="15" cy="5" r="2"/><circle cx="15" cy="25" r="2"/><circle cx="5" cy="15" r="2"/><circle cx="25" cy="15" r="2"/><path d="M15 7v5M15 18v5M7 15h5M18 15h5"/></svg></div>
    <h3>Blockchain Business</h3>
    <p>Lorem ipsum dolor sit amet, consec-tetur adipiscing elit, sed do eiusmod tempor incididunt</p>
    <div class="learn">Learn More <svg width="13" height="13" viewBox="0 0 13 13"><circle cx="6.5" cy="6.5" r="6.5" fill="#fff"/><path d="M5 3.5l3 3-3 3" stroke="#0b0936" stroke-width="1.6" fill="none"/></svg></div>
  </div>
</section>

<section class="tutorials">
  <h2 class="section-title" style="top:1160px">CoinHarbor Tutorial</h2>
  <div class="pill pill-white" style="left:428px;top:1228px;width:185px;height:50px;font-size:17px;font-weight:500">Tutorial Videos</div>
  <div class="pill pill-outline" style="left:634px;top:1228px;width:138px;height:50px;font-size:17px;font-weight:500">Podcast</div>

  <article class="card" style="left:112px;top:1317px;background:linear-gradient(180deg,#0a0a1e,#1a0f2e 70%,#3a1430)" role="img" aria-label="Tutorial thumbnail: pixel-art night sky">
    <div class="card-social"><span>Chirpline</span><span>Snapmosaic</span><span>Wirepost</span></div>
    <div class="card-badge">Free</div>
    <div class="card-foot"><small>CoinHarbor</small><strong>Nft Tutorial</strong><div class="watch">&#9654; Watch Now</div></div>
  </article>
  <article class="card" style="left:446px;top:1317px;background:linear-gradient(180deg,#1d2a6a,#3a2050 45%,#8a2a40 65%,#2a5ab0)" role="img" aria-label="Tutorial thumbnail: pixel-art NFT artwork">
    <div class="card-social"><span>Chirpline</span><span>Snapmosaic</span><span>Wirepost</span></div>
    <div class="card-badge">Paid</div>
    <div class="card-foot"><small>20% Discount</small><strong>Nft Tutorial</strong><div class="watch">&#9654; Watch Now</div></div>
  </article>
  <article class="card" style="left:780px;top:1317px;background:linear-gradient(180deg,#1a3a8a,#142a6a 60%,#0e1a44)" role="img" aria-label="Tutorial thumbnail: pixel-art moonlit landscape">
    <div class="card-social"><span>Chirpline</span><span>Snapmosaic</span><span>Wirepost</span></div>
    <div class="card-badge">Free</div>
    <div class="card-foot"><small>CoinHarbor</small><strong>Nft Tutorial</strong><div class="watch">&#9654; Watch Now</div></div>
  </article>
  <article class="card" style="left:112px;top:1686px;background:linear-gradient(180deg,#9cc4d8,#8cc0e0 70%,#1e7ad0)" role="img" aria-label="Tutorial thumbnail: pixel-art sunny seascape">
    <div class="card-social"><span>Chirpline</span><span>Snapmosaic</span><span>Wirepost</span></div>
    <div class="card-badge">Paid</div>
    <div class="card-foot"><small>20% Discount</small><strong>Nft Tutorial</strong><div class="watch">&#9654; Watch Now</div></div>
  </article>
  <article class="card" style="left:446px;top:1686px;background:linear-gradient(180deg,#0f3a4a,#1a5a6a 35%,#2a3a44 60%,#123a3a)" role="img" aria-label="Tutorial thumbnail: pixel-art mountain landscape">
    <div class="card-social"><span>Chirpline</span><span>Snapmosaic</span><span>Wirepost</span></div>
    <div class="card-badge">Free</div>
    <div class="card-foot"><small>CoinHarbor</small><strong>Nft Tutorial</strong><div class="watch">&#9654; Watch Now</div></div>
  </article>
  <article class="card" style="left:780px;top:1686px;background:linear-gradient(180deg,#1a1aa0,#3a20c0 45%,#a030c0 70%,#1a4a3a)" role="img" aria-label="Tutorial thumbnail: pixel-art forest at night">
    <div class="card-social"><span>Chirpline</span><span>Snapmosaic</span><span>Wirepost</span></div>
    <div class="card-badge">Paid</div>
    <div class="card-foot"><small>20% Discount</small><strong>Nft Tutorial</strong><div class="watch">&#9654; Watch Now</div></div>
  </article>
</section>

<section class="education">
  <div class="edu-band"></div>
  <h2 class="section-title" style="top:2162px;font-size:40px">Digital Asset Education</h2>
  <p class="edu-text">Lorem ipsum dolor sit amet, consectetur adipiscing elit, sed do eiusmod tempor incididunt ut labore et dolore magna aliqua. Quis ipsum suspendisse ultrices gravida. Risus commodo</p>
  <div class="pill pill-white" style="left:450px;top:2303px;width:100px;height:47px;font-size:15px;font-weight:500">Blogs</div>
  <div class="pill pill-outline" style="left:565px;top:2303px;width:186px;height:47px;font-size:15px">Check Your Result</div>
</section>

<section class="nft-education">
  <h2 class="section-title" style="top:2488px">NFT Education</h2>
  <article class="nft" style="left:-4px;top:2623px;width:336px;height:352px">
    <div class="nft-art" style="height:284px;background:linear-gradient(180deg,#7a2ad0,#3a4ad8 45%,#2a6ad0 70%,#3ab0a0)" role="img" aria-label="Tutorial artwork: pixel-art planet landscape"></div>
    <div class="nft-cap" style="font-size:20px;line-height:68px">CoinHarbor Tutorial</div>
  </article>
  <article class="nft" style="left:393px;top:2585px;width:407px;height:432px">
    <div class="nft-art" style="height:345px;background:linear-gradient(180deg,#8ad8f0,#9ae0f8 60%,#4aa030 72%,#6a3a20)" role="img" aria-label="Tutorial artwork: pixel-art platform game scene"></div>
    <div class="nft-cap" style="font-size:24px;line-height:87px">CoinHarbor Tutorial</div>
  </article>
  <article class="nft" style="left:862px;top:2623px;width:340px;height:352px">
    <div class="nft-art" style="height:284px;background:linear-gradient(180deg,#e0a0d0,#c060a8 40%,#f0e0f0 65%,#8a6ab0)" role="img" aria-label="Tutorial artwork: pixel-art pink clouds"></div>
    <div class="nft-cap" style="font-size:20px;line-height:68px">CoinHarbor Tutorial</div>
  </article>
  <span class="dot" style="left:571px"></span>
  <span class="dot" style="left:593px;background:var(--blue)"></span>
  <span class="dot" style="left:615px"></span>
</section>

<footer>
  <div class="brand" style="left:112px;top:3243px"><span class="brand-dot"></span>CoinHarbor Rangers</div>
  <div class="foot-head" style="left:112px;top:3332px">Quick Link</div>
  <ul class="foot-list" style="left:112px;top:3376px;line-height:25.5px">
    <li>Home</li><li>About</li><li>Nft</li><li>Invaders</li><li>Contact</li>
  </ul>
  <div class="foot-head" style="left:324px;top:3334px">Help Link</div>
  <ul class="foot-list" style="left:324px;top:3376px;line-height:30px;font-size:14px">
    <li>Terms&amp;condtions</li><li>Privacy Policy</li><li>About Us</li><li>Support</li>
  </ul>

  <h2 class="news-title">Join Our Newsletter</h2>
  <div class="news-input">Enter Your Email</div>
  <div class="pill" style="left:943px;top:3313px;width:126px;height:36px;background:var(--blue);font-size:14px;font-weight:500">Join Now</div>
  <div class="abs" style="left:586px;top:3381px;font-size:14px;font-weight:700;white-space:nowrap">0-400-555-0142 &nbsp;&nbsp; hello@coinharbor.example</div>
  <div class="abs" style="left:930px;top:3384px;display:flex;gap:6px;font-size:10px;white-space:nowrap">
    <span>Snapmosaic</span><span>Chirpline</span>
  </div>
  <div class="wallet" style="left:585px"><i style="background:#e8802a"></i>VaultPorch</div>
  <div class="wallet" style="left:758px;color:#3a6af0"><i style="background:var(--white)"></i>Keel Purse</div>

  <div class="abs" style="left:112px;top:3555px;font-size:15px;white-space:nowrap">&copy;Copyrights 2022 &nbsp;CoinHarbor Rangers &nbsp;| &nbsp;&nbsp;All Rights Reserved</div>
  <div class="pay" aria-label="Accepted payment methods">
    <span style="background:#3a3a3a"></span><span></span><span></span><span></span><span></span><span style="background:#2a6ad0"></span><span></span>
  </div>
</footer>

</body>
</html>
```